Pawn Shop Website

I want my site to be similar to quillbarter.net. Except, I will not be selling anything off the site. Would rather it just be informational. I have a logo which I would like to use.

Also, I do not need this site to be perfect. I will do a lot of altering myself and I would typically design the entire page myself but am overwhelmed with other responsibilities. Plus, you guys are great here and i've used this service before and you really give great ideas. So, I'm just looking for a template. I can handle making a flash banner, but it will give you kudos points if included.
Updates

Also, I want the colors to be Gray and Black for background.  Then for the fonts Gold inside and Green outline.  I will be posting the information for my logo once I get to my other computer.

Industry/Entity Type

Shop

Requirements
Must have
• Main location
4127 W Hollister Ave
Stone Park, IL 60892
555-862-1937

other location
Brindle Cove Pawn Shop
2805 E Fenwick St.
Melrose Park, IL 60847
555-317-4086

```html
<!DOCTYPE html>
<html lang="en">
<head>
<meta charset="utf-8">
<title>Quill Barter Pawn</title>
<link href="https://fonts.googleapis.com/css2?family=PT+Sans:wght@400;700&family=Oswald:wght@500&display=swap" rel="stylesheet">
<style>
:root{
  --page:#f4f4f4;
  --header:#1e1e1e;
  --nav-text:#333;
  --panel-line:#d4d4d4;
  --text:#6e6e6e;
  --heading:#4a4a4a;
  --gold:#f2c200;
  --link-gold:#e0a800;
  --footer:#d1d0d0;
  --footer-text:#8a8a8a;
  --base:#1f1f1f;
}
*{box-sizing:border-box;margin:0;padding:0}
html,body{width:1200px;height:1198px;overflow:hidden}
body{background:var(--page);font-family:"PT Sans",sans-serif;color:var(--text);position:relative}
.site-header{position:absolute;left:120px;top:0;width:960px;height:154px;background:linear-gradient(170deg,#2a2a2a,#161616)}
.brand{position:absolute;left:28px;top:56px;display:flex;align-items:center;gap:10px;font-weight:700;font-size:40px;color:var(--gold);text-transform:uppercase;letter-spacing:1px}
.brand-mark{width:22px;height:22px;border-radius:50%;background:var(--gold)}
.main-nav{position:absolute;left:120px;top:154px;width:960px;height:40px;background:linear-gradient(#f7f7f7,#e2e2e2);border:1px solid #d0d0d0;display:flex;font-family:"Oswald",sans-serif;font-size:18px;color:var(--nav-text);text-transform:uppercase}
.main-nav a{color:inherit;text-decoration:none;line-height:40px;padding:0 17px}
.main-nav a.active{background:#fff;padding:0 24px 0 29px;border-right:1px solid #d0d0d0}
.panel{position:absolute;background:linear-gradient(#ededed,#f8f8f8);border:1px solid var(--panel-line)}
.locations{left:120px;top:214px;width:251px;height:360px;padding:23px 8px 0 27px}
.locations h2{font-size:19px;line-height:24px;font-weight:400;color:var(--heading);margin-bottom:8px}
.locations .address{font-size:14px;line-height:18px}
.locations .links{font-size:10px;line-height:12px;text-align:right;color:#555}
.locations .links span{color:var(--link-gold)}
.divider{border:0;border-top:1px solid #d8d8d8;margin:4px -8px 18px -20px}
.divider.last{margin-bottom:13px}
.locations .note{font-size:12px;line-height:18px;font-weight:700;color:#777}
.down-arrow{position:absolute;left:113px;bottom:5px}
.slider{position:absolute;left:391px;top:214px;width:687px;height:360px;border:1px solid #d8d8d8;background:linear-gradient(100deg,#ffffff 40%,#e9e6e1 70%,#5b6373 90%)}
.slider-bar{position:absolute;left:0;bottom:0;width:100%;height:17px;background:rgba(220,220,220,.8)}
.dots{position:absolute;right:8px;top:3px;display:flex;gap:3px}
.dots i{width:11px;height:11px;border-radius:50%;background:#3a3a3a}
.dots i.light{background:#bbb}
.aside{left:118px;top:596px;width:251px;height:338px;padding:20px 10px 0 22px}
.aside h2{font-size:20px;font-weight:400;color:var(--heading);text-align:center;margin-bottom:14px}
.aside p{font-size:16px;line-height:22px}
.content{position:absolute;left:399px;top:608px;width:678px}
.content h1{font-size:24px;font-weight:400;color:#3e3e3e;margin-bottom:6px}
.content p{font-size:16px;line-height:22px;letter-spacing:.35px;margin-bottom:19px}
.site-footer{position:absolute;left:120px;top:957px;width:960px;height:183px;background:var(--footer);border-top:3px solid #bcbcbc}
.col{position:absolute;top:24px}
.col h3{font-size:14px;font-weight:400;color:#333;text-transform:uppercase;margin-bottom:4px}
.col li{list-style:none;font-size:12px;line-height:18px;font-weight:700;color:var(--footer-text);padding-left:1px}
.col p{font-size:12px;line-height:18px;font-weight:700;color:var(--footer-text);width:290px}
.base{position:absolute;left:120px;top:1140px;width:960px;height:58px;background:var(--base);font-size:11px;font-weight:700;color:#8c8c8c}
.copyright{position:absolute;left:30px;top:27px}
.follow{position:absolute;right:20px;top:18px;display:flex;align-items:center;gap:6px}
.follow span{margin-right:4px}
.follow i{width:30px;height:29px;background:#6f6f6f;border:1px solid #9a9a9a}
</style>
</head>
<body>
<header class="site-header">
  <div class="brand"><span class="brand-mark"></span>Quill Barter Pawn</div>
</header>
<nav class="main-nav">
  <a class="active" href="#">Home</a>
  <a href="#">In Store Coupons</a>
  <a href="#">About the Store</a>
  <a href="#">Pawn FAQ</a>
  <a href="#">General FAQ</a>
  <a href="#">Contact/Map</a>
  <a href="#">Photos &amp; Videos</a>
</nav>

<section class="panel locations">
  <h2>Main location</h2>
  <p class="address">4127 W Hollister Ave<br>Stone Park, IL 60892<br>555-862-1937</p>
  <p class="links"><span>View Map</span> | See more..</p>
  <hr class="divider">
  <h2>Other Location</h2>
  <p class="address">Brindle Cove Pawn Shop<br>2805 E Fenwick St.<br>Melrose Park, IL 60847<br>555-317-4086</p>
  <p class="links"><span>View Map</span> | See more..</p>
  <hr class="divider last">
  <p class="note">Lorem Ipsum Lorem Ipsum Lorem Ipsum Lorem Ipsum Lorem Ipsum Lorem Ipsum....</p>
  <svg class="down-arrow" width="18" height="16" viewBox="0 0 18 16"><path d="M0 0h18L9 16z" fill="#9a9a9a"/></svg>
</section>

<section class="slider" role="img" aria-label="Banner photo: a hand tossing a smartphone against a white backdrop">
  <div class="slider-bar"><div class="dots"><i></i><i class="light"></i><i class="light"></i><i></i></div></div>
</section>

<aside class="panel aside">
  <h2>Put Anything Here</h2>
  <p>Lorem Ipsum is simply dummy text of the printing and type setting industry. Lorem Ipsum has been the industry's stan dard dummy text ever since the 1500s, when an unknown printer took</p>
  <p style="margin-top:22px">a galley of type and scrambled it to make a type specimen book. It has survived not only five ..</p>
</aside>

<main class="content">
  <h1>Lorem Ipsum</h1>
  <p>Lorem Ipsum is simply dummy text of the printing and typesetting industry. Lorem Ipsum has been the industry's standard dummy text ever since the 1500s, when an unknown printer took a galley of type and scrambled it to make a type specimen book. It has survived not only five centuries, but also the leap into electronic typesetting, remaining essentially unchanged. It was popularised in the 1960s with the release of Typeline sheets containing Lorem Ipsum passages, and more recently with desktop publishing software like Pagewright Studio including versions of Lorem Ipsum.</p>
  <p>Lorem Ipsum is simply dummy text of the printing and typesetting industry. Lorem Ipsum has been the industry's standard dummy text ever since the 1500s, when an unknown printer took a galley of type and scrambled it to make a type specimen book. It has survived not only five centuries, but also the leap into electronic typesetting, remaining essentially unchanged. It was popularised in the 1960s with the release of Typeline..</p>
</main>

<footer class="site-footer">
  <div class="col" style="left:14px"><h3>Services</h3><ul><li>Rest House</li><li>City Life</li><li>Vacation</li><li>Family Reunion</li><li>Friends on Vacation</li><li>Study Hotel</li></ul></div>
  <div class="col" style="left:176px"><h3>Services</h3><ul><li>Rest House</li><li>City Life</li><li>Vacation</li><li>Family Reunion</li><li>Friends on Vacation</li><li>Study Hotel</li></ul></div>
  <div class="col" style="left:350px"><h3>Services</h3><ul><li>Rest House</li><li>City Life</li><li>Vacation</li><li>Family Reunion</li><li>Friends on Vacation</li><li>Study Hotel</li></ul></div>
  <div class="col" style="left:651px"><h3>About Us</h3><p>Nestled snugly at the foot of the Bavarian Alps, it's easy to see why Halvorsen was so inspired growing up in this city. It may be number 44 on our list but Salzburg continues to be number one for avid fans of The Valley Song!</p></div>
</footer>
<div class="base">
  <div class="copyright">COPYRIGHT 2012-2013 by QUILL BARTER PAWN</div>
  <div class="follow"><span>FOLLOW US:</span><i></i><i></i><i></i></div>
</div>
</body>
</html>
```